Barrister at Law needs Business Card Design

Need a business card design for Barrister at Law. Double sided. Simple Tom Wexley and Barrister at Law on one side with contact details on the other side. I would like a professional design using Black or Platinum. Details on reverse side would include qualifications - Bcom-Llb and Acc Spec Commercial Litigation. I have attached the logo. Contact details would include address/ Po Box/ Phone/Fax/Mobile/email. I would like to use raised print or spot gloss.

```html
<!DOCTYPE html>
<html lang="en">
<head>
<meta charset="utf-8">
<title>Tom Wexley – Barrister-at-Law Business Card</title>
<link rel="stylesheet" href="https://fonts.googleapis.com/css2?family=Cinzel:wght@400;500&family=Nunito+Sans:wght@400&display=swap">
<style>
  :root {
    --page-bg: #e9e6e2;
    --card-bg: #2b2b2c;
    --accent-blue: #1e7bc0;
    --text-grey: #b9b9b9;
    --subtitle-grey: #a9a9a9;
    --emboss-dark: #18181a;
    --mark-grey: #3b3b3d;
  }
  * { margin: 0; padding: 0; box-sizing: border-box; }
  html, body {
    width: 1200px; height: 1000px; overflow: hidden;
    background: var(--page-bg);
  }
  .canvas { position: relative; width: 1200px; height: 1000px; }
  .card {
    position: absolute; left: 265px; width: 665px; height: 397px;
    background: var(--card-bg); border-radius: 22px;
  }
  .card--details { top: 73px; }
  .card--name { top: 533px; }

  .name {
    font-family: "Cinzel", serif; font-weight: 500; text-transform: uppercase;
    color: var(--accent-blue); white-space: nowrap; line-height: 1;
  }
  .title {
    font-family: "Cinzel", serif; font-weight: 400; text-transform: uppercase;
    white-space: nowrap; line-height: 1;
  }
  .card--details .name {
    position: absolute; left: 51px; top: 43px; font-size: 30px; letter-spacing: 0.6px;
  }
  .card--details .title {
    position: absolute; left: 52px; top: 80px; font-size: 17px; letter-spacing: 3.6px;
    color: var(--subtitle-grey);
  }
  .body-text {
    font-family: "Nunito Sans", sans-serif; font-size: 16px; color: var(--text-grey);
    line-height: 23.5px;
  }
  .qualifications { position: absolute; left: 52px; top: 120px; font-size: 15.5px; }
  .address { position: absolute; left: 52px; top: 183px; font-style: normal; }
  .contact-list { position: absolute; left: 52px; top: 265px; list-style: none; }
  .contact-list li { display: flex; align-items: center; height: 24px; }
  .contact-list svg { width: 13px; height: 13px; margin-right: 8px; fill: var(--accent-blue); }

  .brand-mark {
    position: absolute; left: 400px; top: 100px; width: 200px; height: 240px;
    display: flex; align-items: center; justify-content: center;
    font-family: "Cinzel", serif; font-weight: 500; font-size: 24px; text-transform: uppercase;
    color: var(--mark-grey); white-space: nowrap;
  }

  .card--name .name {
    position: absolute; left: 0; right: 0; top: 160px; text-align: center;
    font-size: 44px; letter-spacing: 0.8px;
  }
  .card--name .title {
    position: absolute; left: 0; right: 0; top: 212px; text-align: center;
    font-size: 24px; letter-spacing: 6.5px; color: var(--emboss-dark);
  }
</style>
</head>
<body>
<main class="canvas">
  <section class="card card--details" aria-label="Card front with contact details">
    <h1 class="name">Tom Wexley</h1>
    <p class="title">Barrister-at-Law</p>
    <p class="body-text qualifications">B.COM-LL.B. Acc. Spec. (Com. Lit.)</p>
    <address class="body-text address">
      Marlow Chambers<br>
      Level 1, 42 Marlow Street<br>
      BRAYFIELD Qld 4870
    </address>
    <ul class="body-text contact-list">
      <li><svg viewBox="0 0 13 13" aria-label="Mobile"><path d="M3.5 0h6a1 1 0 0 1 1 1v11a1 1 0 0 1-1 1h-6a1 1 0 0 1-1-1V1a1 1 0 0 1 1-1zm.5 1.5v8.5h5V1.5zm2.5 9.3a.7.7 0 1 0 0 1.4.7.7 0 0 0 0-1.4z" fill-rule="evenodd"/></svg>0412 508 316</li>
      <li><svg viewBox="0 0 13 13" aria-label="Phone"><path d="M0 4c0-2 3-3 6.5-3S13 2 13 4v1.2H9.6V3.8H3.4v1.4H0zM3 6l1.5-1.8h4L10 6l2 4v2H1v-2zm3.5 1a1.6 1.6 0 1 0 0 3.2 1.6 1.6 0 0 0 0-3.2z" fill-rule="evenodd"/></svg>07 4790 2284</li>
      <li><svg viewBox="0 0 13 13" aria-label="Fax"><path d="M3 0h7v3H3zM1 4h11a1 1 0 0 1 1 1v5h-2.5V8h-8v2H0V5a1 1 0 0 1 1-1zm2.5 5h6v4h-6z"/></svg>07 4790 226</li>
      <li><svg viewBox="0 0 13 13" aria-label="Email"><path d="M0 3h13v.8L6.5 8 0 3.8zm0 2l6.5 4.2L13 5v6H0z"/></svg>twexley@wexleybar.com.au</li>
    </ul>
    <div class="brand-mark">Tom Wexley</div>
  </section>

  <section class="card card--name" aria-label="Card back with name">
    <h2 class="name">Tom Wexley</h2>
    <p class="title">Barrister-at-Law</p>
  </section>
</main>
</body>
</html>
```